Website Revamp to a Legal Tech Company

We are a Legal Technology Company and we are revamping our whole company from the logo (already done) to the website. We have built a custom portal and harnessed the use of AI and automation.

Current Website - https://www.verantiq.com/

We need a new website that looks like a tech company
Some examples of websites for samples
1. What we have today - https://www.verantiq.com/
2. https://plumbrivet.com/
3. https://www.mossferns.com/
4. https://www.tavu.com/
5.https://www.brightkolaw.com/
6. https://www.sudorapt.com/

Hope this helps. Let's start with the Home page.
Once we agree on the basis design and the first 3-4 pages - we can handle the coding etc. Will have the content over once we have the basic homepage design.

Links that we will possibly have and want
1. Home
2. About Us
3. Place your Order
4. Free First File offer to all new customers
5. Services/Products
6. Transparent Pricing
7. Contact Us

Terms & Conditions and Privacy Policy will be added at the bottom of the page but our internal designers.

Hope this helps.

Target Market(s)

Personal Injury Law Firms in the US

Industry/Entity Type

Legal Tech Services

Coding

Coded - Design and coding required

Number of Pages Required

4 page

Colors

Designer to choose colors to be used in the design.

Requirements
Must have
• Need to look like a Tech company website
Nice to have
• The color Blue

```html
<!DOCTYPE html>
<html lang="en">
<head>
<meta charset="utf-8">
<title>Verantiq AI — Legal Tech Solutions</title>
<link href="https://fonts.googleapis.com/css2?family=Crimson+Pro:wght@400;500&family=Poppins:wght@400;500;600&display=swap" rel="stylesheet">
<style>
:root{
  --navy:#062c4f;
  --blue:#0d4f8c;
  --blue-bright:#1460b4;
  --ink:#2a3440;
  --muted:#5e6874;
  --page:#f4f5f7;
  --white:#ffffff;
}
*{box-sizing:border-box;margin:0;padding:0}
html,body{width:1200px;height:3224px;overflow:hidden}
body{background:var(--page);font-family:"Poppins",sans-serif;color:var(--ink);position:relative}
.abs{position:absolute}
.frame{position:absolute;left:65px;top:69px;width:1050px;height:3089px;background:var(--white);box-shadow:0 4px 20px rgba(10,30,60,.08);overflow:hidden}
.header{position:absolute;left:0;top:0;width:100%;height:57px;background:#fff;border-bottom:1px solid #eef1f5}
.brand{position:absolute;display:flex;align-items:center;gap:6px;font-family:"Crimson Pro",serif;font-weight:500;color:var(--navy)}
.brand .dot{width:14px;height:14px;border-radius:50%;background:var(--blue)}
.nav{position:absolute;left:310px;top:21px;display:flex;gap:22px;font-family:"Crimson Pro",serif;font-size:11px;color:var(--ink)}
.nav .active{color:var(--blue);position:relative}
.nav .active::after{content:"";position:absolute;left:0;right:0;top:32px;height:2px;background:var(--blue)}
.btn{display:inline-flex;align-items:center;gap:6px;border-radius:20px;font-family:"Crimson Pro",serif;font-size:10px;padding:0 18px;height:28px}
.btn.solid{background:var(--blue);color:#fff}
.btn.ghost{border:1px solid var(--blue);color:var(--blue);background:#fff}
.btn.ghost-light{border:1px solid #fff;color:#fff}
.btn.text-light{color:#fff;padding:0 6px}
.hero{position:absolute;left:0;top:57px;width:100%;height:525px;background:linear-gradient(180deg,#fff 0%,#f3f7fc 100%)}
.hero h1{position:absolute;left:151px;top:130px;width:380px;font-family:"Crimson Pro",serif;font-weight:400;font-size:35px;line-height:39px;color:var(--ink)}
.hero h1 b{font-family:"Poppins",sans-serif;font-weight:600;color:var(--blue);font-size:30px}
.hero p{position:absolute;left:151px;top:258px;width:345px;font-size:10px;line-height:19px;color:var(--muted)}
.photo{position:absolute;border-radius:50%}
.dark{position:absolute;left:0;top:582px;width:100%;height:482px;background:var(--navy)}
.dark h2{position:absolute;left:524px;top:116px;font-family:"Crimson Pro",serif;font-weight:400;font-size:26px;color:#fff}
.dark h2 b{font-family:"Poppins",sans-serif;font-weight:600;font-size:20px}
.dark p{position:absolute;left:524px;width:380px;font-size:9.5px;line-height:19px;color:#c9d6e6}
.sec-title{position:absolute;left:0;width:100%;text-align:center;font-family:"Crimson Pro",serif;font-weight:400;font-size:23px;color:var(--ink)}
.services{position:absolute;left:0;top:1064px;width:100%;height:507px;background:#f8f9fb}
.svc{position:absolute;top:118px;width:365px;height:313px;background:linear-gradient(180deg,#fff 0%,#f3f6fb 100%);border-radius:6px;box-shadow:0 4px 16px rgba(10,30,60,.08);padding:40px 38px}
.svc h3{font-family:"Crimson Pro",serif;font-weight:400;font-size:25px;line-height:29px;color:var(--blue)}
.svc p{font-size:8.5px;line-height:15px;color:var(--muted);margin-top:16px}
.svc .btn{margin-top:26px}
.why{position:absolute;left:0;top:1571px;width:100%;height:483px;background:linear-gradient(180deg,#fff 0%,#f0f5fb 100%)}
.why-card{position:absolute;width:347px;height:100px;background:#fff;border-radius:6px;box-shadow:0 4px 16px rgba(10,30,60,.08);padding:24px 20px 0 66px}
.why-card .ico{position:absolute;left:20px;top:28px;width:34px;height:34px;border-radius:50%;background:var(--blue);display:flex;align-items:center;justify-content:center}
.why-card h3{font-family:"Crimson Pro",serif;font-weight:400;font-size:16px;color:var(--ink)}
.why-card p{font-size:8.5px;line-height:15px;color:var(--muted);margin-top:6px}
.blogs{position:absolute;left:0;top:2054px;width:100%;height:467px;background:linear-gradient(180deg,var(--navy) 0%,#0a2d55 80%,#1a2c60 100%)}
.blogs .sec-title{color:#fff}
.post{position:absolute;top:123px;width:173px;height:223px;background:#fff;border-radius:5px;padding:5px}
.post .thumb{height:117px;border-radius:3px}
.post h4{font-family:"Crimson Pro",serif;font-weight:500;font-size:8.5px;line-height:10px;color:var(--blue);margin:11px 6px 0}
.post p{font-size:7px;line-height:11px;color:var(--muted);margin:5px 6px 0}
.post .more{font-family:"Crimson Pro",serif;font-size:8.5px;color:var(--blue);margin:6px 6px 0}
.contact{position:absolute;left:0;top:2521px;width:100%;height:488px;background:#f8f9fb}
.panel{position:absolute;top:56px;height:377px;background:#fff;border-radius:6px;box-shadow:0 4px 16px rgba(10,30,60,.08)}
.panel h3{font-family:"Crimson Pro",serif;font-weight:500;font-size:20px;color:var(--blue-bright)}
.field{height:27px;border-radius:5px;background:#f3f5f8;font-size:9px;color:var(--muted);padding:8px 13px;margin-bottom:14px}
.info{display:flex;gap:9px;font-size:9px;line-height:15px;color:var(--muted);margin-top:10px}
.footer{position:absolute;left:0;top:3009px;width:100%;height:80px;background:#fff}
.footnav{position:absolute;left:508px;top:33px;display:flex;gap:30px;font-family:"Crimson Pro",serif;font-size:10px;color:var(--ink)}
</style>
</head>
<body>
<div class="frame">

  <header class="header">
    <div class="brand" style="left:151px;top:18px;font-size:16px"><span class="dot"></span>Verantiq AI</div>
    <nav class="nav">
      <span class="active">Home</span><span>About</span><span>Services ⌄</span><span>Who we help ⌄</span><span>Pricing ⌄</span><span>Case type ⌄</span><span>Resources ⌄</span>
      <svg width="12" height="12" viewBox="0 0 12 12"><circle cx="5" cy="5" r="3.8" fill="none" stroke="#0d4f8c" stroke-width="1.3"/><line x1="8" y1="8" x2="11" y2="11" stroke="#0d4f8c" stroke-width="1.3"/></svg>
    </nav>
    <span class="btn solid abs" style="left:806px;top:14px">Contact Us <span>→</span></span>
  </header>

  <section class="hero">
    <h1>Empowering Law Firms with <b>AI-Driven</b> Legal Tech Solutions</h1>
    <p>Verantiq employs a team with expertise in retrieving, assembling, reviewing, and medical records and bills.</p>
    <span class="btn solid abs" style="left:151px;top:321px">Contact Us <span>→</span></span>
    <div class="photo" role="img" aria-label="Photo of a smiling professional woman holding a clipboard, with floating progress and chart cards" style="left:571px;top:80px;width:328px;height:328px;background:linear-gradient(160deg,#2a66a6 0%,#7fa6cc 55%,#e6eef7 100%)"></div>
  </section>

  <section class="dark">
    <div class="photo" role="img" aria-label="Photo of a businessman in a suit reading a tablet, with a floating progress card" style="left:151px;top:77px;width:328px;height:328px;background:linear-gradient(150deg,#c9c7c2 0%,#8c8a88 50%,#2a2d33 100%)"></div>
    <h2>Organized Medical Verantiq <b>AI</b></h2>
    <p style="top:159px">Verantiq employs a team with expertise in retrieving, assembling, reviewing, and summarizing medical records and bills. We support law firms by handling all medical records-related tasks, thereby allowing attorneys to focus on other very important case-related matters, such as proving liability, causation, and damages.</p>
    <p style="top:259px">Verantiq is equipped to immediately handle any size project for a small, mid-sized, or large law firm. Our team works within a secure facility and adheres to the highest level of security and confidentiality in order to safeguard your client's records and privacy.</p>
    <span class="btn ghost-light abs" style="left:524px;top:346px">Read More <span>→</span></span>
    <span class="btn text-light abs" style="left:620px;top:346px">Contact Us <span>→</span></span>
  </section>

  <section class="services">
    <h2 class="sec-title" style="top:79px">Our Services</h2>
    <div class="svc" style="left:151px">
      <h3>Seasoned Medico-Legal Professionals</h3>
      <p>Easy-to-use Summaries. Supporting pieces of evidence.<br>Prepared by Experts</p>
      <p style="margin-top:13px">Partnering with several law firms, we have developed expertise in various litigation support documentation services to support attorneys that handle case types such as Personal Injury, Medical Malpractice, and Mass Tort cases.</p>
      <span class="btn ghost">Read More <span>→</span></span>
    </div>
    <div class="svc" style="left:534px">
      <h3>Medical Record Retrieval and Review Services</h3>
      <p>Organized medical records summaries that help you settle cases and claims faster.</p>
      <p style="margin-top:13px">Verantiq's team includes seasoned professionals with in-depth clinical knowledge so that you get unparalleled medico-legal services with a high degree of accuracy and reliability.</p>
      <span class="btn ghost">Read More <span>→</span></span>
    </div>
  </section>

  <section class="why">
    <h2 class="sec-title" style="top:156px">Why Verantiq</h2>
    <svg class="abs" style="left:405px;top:200px" width="240" height="240" viewBox="0 0 240 240">
      <circle cx="120" cy="120" r="60" fill="none" stroke="#c9d6e6" stroke-dasharray="4 6"/>
      <circle cx="120" cy="120" r="90" fill="none" stroke="#dbe4ef" stroke-dasharray="4 6"/>
    </svg>
    <div class="why-card" style="left:151px;top:205px">
      <span class="ico"><svg width="16" height="16" viewBox="0 0 16 16"><rect x="3" y="2" width="10" height="12" rx="1" fill="none" stroke="#fff" stroke-width="1.3"/><line x1="5.5" y1="6" x2="10.5" y2="6" stroke="#fff"/><line x1="5.5" y1="9" x2="10.5" y2="9" stroke="#fff"/></svg></span>
      <h3>Medical Records Solutions</h3>
      <p>We provide medical records solutions to small, mid-sized, or large law firms.</p>
    </div>
    <div class="why-card" style="left:553px;top:205px">
      <span class="ico"><svg width="16" height="16" viewBox="0 0 16 16"><circle cx="5.5" cy="6" r="2.3" fill="none" stroke="#fff" stroke-width="1.3"/><circle cx="10.5" cy="6" r="2.3" fill="none" stroke="#fff" stroke-width="1.3"/><path d="M1.5 13c1-3 7-3 8 0M6.5 13c1-3 7-3 8 0" fill="none" stroke="#fff" stroke-width="1.2"/></svg></span>
      <h3>Highly Trained Staff</h3>
      <p>Our staff has expertise in and received training on retrieving, reviewing, and summarizing medical records.</p>
    </div>
    <div class="why-card" style="left:151px;top:353px">
      <span class="ico"><svg width="16" height="16" viewBox="0 0 16 16"><circle cx="8" cy="8" r="6" fill="none" stroke="#fff" stroke-width="1.3"/><circle cx="8" cy="8" r="3" fill="none" stroke="#fff" stroke-width="1.3"/></svg></span>
      <h3>Highest Quality</h3>
      <p>We provide the highest quality medical records support services that will save your firm money, time, and effort.</p>
    </div>
    <div class="why-card" style="left:553px;top:353px">
      <span class="ico"><svg width="16" height="16" viewBox="0 0 16 16"><path d="M8 1.5l5.5 2v4.5c0 3-2.5 5.5-5.5 6.5C5 13.5 2.5 11 2.5 8V3.5z" fill="none" stroke="#fff" stroke-width="1.2"/><path d="M5.5 8l2 2 3-3.5" fill="none" stroke="#fff" stroke-width="1.2"/></svg></span>
      <h3>HIPAA and HITECH</h3>
      <p>We are HIPAA and HITECH compliant, and our staff follows strict rules-based security protocols.</p>
    </div>
  </section>

  <section class="blogs">
    <h2 class="sec-title" style="top:87px">Blogs</h2>
    <article class="post" style="left:151px">
      <div class="thumb" role="img" aria-label="Photo of a judge's gavel on a desk" style="background:linear-gradient(160deg,#3c3f46,#8a6a4a 70%,#c9a77f)"></div>
      <h4>Intentional Misuse of Social Media App May Lead to Developer Liability</h4>
      <p>Social media and messaging applications have changed the way people communicate.</p>
      <div class="more">Read More →</div>
    </article>
    <article class="post" style="left:342px">
      <div class="thumb" role="img" aria-label="Photo of a lawyer at a desk in a library office" style="background:linear-gradient(160deg,#6b5a48,#2b2e35 60%,#8b7a64)"></div>
      <h4>Intentional Misuse of Social Media App May Lead to Developer Liability</h4>
      <p>Social media and messaging applications have changed the way people communicate.</p>
      <div class="more">Read More →</div>
    </article>
    <article class="post" style="left:533px">
      <div class="thumb" role="img" aria-label="Photo of a lawyer seated at a desk with scales of justice" style="background:linear-gradient(180deg,#f1f1f1,#d9d9d9 60%,#8e8a84)"></div>
      <h4>Intentional Misuse of Social Media App May Lead to Developer Liability</h4>
      <p>Social media and messaging applications have changed the way people communicate.</p>
      <div class="more">Read More →</div>
    </article>
    <article class="post" style="left:725px">
      <div class="thumb" role="img" aria-label="Photo of a lawyer reviewing documents in an office" style="background:linear-gradient(160deg,#e3e3e3,#9a9a9a 60%,#3a3a3a)"></div>
      <h4>Intentional Misuse of Social Media App May Lead to Developer Liability</h4>
      <p>Social media and messaging applications have changed the way people communicate.</p>
      <div class="more">Read More →</div>
    </article>
    <span class="btn ghost-light abs" style="left:478px;top:367px">View All <span>→</span></span>
  </section>

  <section class="contact">
    <div class="panel" style="left:151px;width:295px;padding:34px 28px">
      <h3>Reach Us</h3>
      <p style="font-size:9px;line-height:16px;color:var(--muted);margin-top:12px">We provide medical records solutions to small, mid-sized, or large law firms.</p>
      <h3 style="font-size:15px;margin-top:22px">Contact us at our offices below.</h3>
      <div style="font-size:10px;color:var(--ink);margin-top:14px">Business Inquiries</div>
      <div class="info"><svg width="11" height="13" viewBox="0 0 11 13"><path d="M5.5 12.5S1 7.5 1 5a4.5 4.5 0 0 1 9 0c0 2.5-4.5 7.5-4.5 7.5z" fill="#1460b4"/><circle cx="5.5" cy="5" r="1.6" fill="#fff"/></svg><span>1820 Harbor Lane, Suite 4B, Coral Bay, FL 33199</span></div>
      <div class="info"><svg width="11" height="12" viewBox="0 0 11 12"><path d="M2 1l2.2 2.3-1 1.5a7 7 0 0 0 3 3l1.5-1L10 9l-1.4 2C4.5 11 .5 7 1 2.5z" fill="#1460b4"/></svg><span>(555) 014-2290</span></div>
      <div class="info"><svg width="11" height="9" viewBox="0 0 11 9"><rect width="11" height="9" rx="1" fill="#1460b4"/><path d="M0.5 1l5 4 5-4" fill="none" stroke="#fff"/></svg><span>info@verantiq.com</span></div>
    </div>
    <div class="panel" style="left:464px;width:434px;padding:34px 28px">
      <h3>Leave a message</h3>
      <div style="margin-top:14px">
        <div class="field">Name</div>
        <div class="field">Email</div>
        <div class="field">Phone</div>
        <div class="field">Organization</div>
        <div class="field" style="height:72px">Your Message</div>
      </div>
      <span class="btn solid abs" style="left:325px;top:323px">Submit <span>→</span></span>
    </div>
  </section>

  <footer class="footer">
    <div class="brand" style="left:151px;top:30px;font-size:16px"><span class="dot"></span>Verantiq AI</div>
    <nav class="footnav"><span>About</span><span>Services</span><span>Who we help</span><span>Pricing</span><span>Case type</span><span>Resources</span></nav>
  </footer>

</div>
</body>
</html>
```